Modern book cover design

We are looking for a modern, powerful book cover for a general intrest book about how robots are going to take human jobs in the future.

The book title is "Torvanique"

It also has a strap line "The close of human work and how automatons will supplant it"
Both the title and the strap line should be on the front cover

I have attached a number of book designs I like, and my author picture.

Reason: Some great submissions but none quite have that wow factor

Target Market(s)

This is a general intrest book, but the reader is likely to be male 30-50

Requirements
Must have
• -Title "Torvanique"

-Strap-line "The close of human work and how automatons will supplant it"

-Be compliant with PrintMoraly Cover Design Criteria(www.printmoraly.example)

-Book size : 5.5 x 8.5 inches

-Spine size : 0.625 inches

-Must have one author picture on the back cover(attached)

-Must have the following author description on back cover:
"Tom Hollis is a leading futurologist, technologist, inventor, and entrepreneur. With over twenty years of experience in technology and innovation, Tom has travelled the world seeking out and developing new technologies. As a leading voice on the challenges and benefits of tomorrow’s technology, he has advised some of the world’s leading institutions, including the Grand Chancery, regarding technological preparations for the future. He is the recipient of the centennial founder of the season prize and has appeared on numerous technology and philanthropy television programs, as well as presenting Clever Little Marvels on Robotics."

-Must have the following book description on back cover:
“Torvanique is a look at the rapidly changing face of robotics and how it will revolutionize employment over the next thirty years. Tom Hollis lays out the arguments in favor of and against the mechanization of our society, as well as the advantages and untold risks as we march into this ever-present future.”

-Must have the following quote on the back cover:
"A fascinating look into the future of robotics and their impact on humanity, be prepared to question when robots will replace you - Derek Pallister, Professor of Cybernetics at the University of Castlemere”

-Example barcode

```html
<!DOCTYPE html>
<html lang="en">
<head>
<meta charset="utf-8">
<title>Torvanique — Book Cover</title>
<link rel="stylesheet" href="https://fonts.googleapis.com/css2?family=Cutive&family=Zilla+Slab:ital,wght@0,700;1,400&display=swap">
<style>
  :root {
    --paper: #ffffff;
    --ink: #111111;
    --spine: #000000;
    --spine-ink: #ffffff;
    --photo-light: #8a8a8a;
    --photo-dark: #2a2a2a;
    --robot-light: #eeeef0;
    --robot-mid: #b9bcc2;
    --robot-dark: #3a4148;
  }
  * { margin: 0; padding: 0; box-sizing: border-box; }
  html, body { width: 1200px; height: 873px; overflow: hidden; background: var(--paper); }
  .cover {
    position: relative;
    width: 1200px; height: 873px;
    background: var(--paper);
    color: var(--ink);
    font-family: "Cutive", "Courier New", serif;
  }
  .back-blurb {
    position: absolute; left: 33px; top: 38px; width: 530px;
    font-family: "Zilla Slab", Georgia, serif;
    font-weight: 700; font-size: 13.4px; line-height: 18.4px;
  }
  .endorsement {
    position: absolute; left: 127px; top: 316px; width: 345px;
    font-family: "Zilla Slab", Georgia, serif;
    font-style: italic; font-size: 13.4px; line-height: 17.4px;
  }
  .author-photo {
    position: absolute; left: 84px; top: 554px; width: 109px; height: 158px;
    background: linear-gradient(160deg, var(--photo-light), var(--photo-dark));
  }
  .author-bio {
    position: absolute; left: 204px; top: 558px; width: 352px;
    font-size: 12.3px; line-height: 18.5px;
  }
  .spine {
    position: absolute; left: 563px; top: 0; width: 97px; height: 873px;
    background: var(--spine);
  }
  .spine-title {
    position: absolute; left: 0; right: 0; top: 425px;
    text-align: center; color: var(--spine-ink);
    font-family: "Zilla Slab", Georgia, serif;
    font-weight: 700; font-size: 12.5px;
  }
  .front-title {
    position: absolute; left: 674px; top: 10px;
    font-family: "Cutive", "Courier New", serif;
    font-weight: 400; font-size: 84px; line-height: 1;
    letter-spacing: -2px;
  }
  .strapline {
    position: absolute; left: 808px; top: 126px; width: 370px;
    font-family: "Zilla Slab", Georgia, serif;
    font-weight: 700; font-size: 21px; line-height: 28px;
  }
  .robot-illustration {
    position: absolute; left: 812px; top: 372px; width: 326px; height: 462px;
    border-radius: 40px 40px 12px 12px;
    background: linear-gradient(180deg, var(--robot-light) 0%, var(--robot-mid) 55%, var(--robot-dark) 100%);
  }
</style>
</head>
<body>
<main class="cover">
  <section class="back-cover">
    <p class="back-blurb">Torvanique is a look at the rapidly changing face of robotics and how it will revolutionize employment over the next thirty years. Tom Hollis lays out the arguments in favor of and against the mechanization of our society, as well as the advantages and untold risks as we march into this ever-present future.</p>
    <blockquote class="endorsement">"A fascinating look into the future of robotics and their impact on humanity, be prepared to question when robots will replace you."<br>Derek Pallister, Professor of Cybernetics at the University of Castlemere</blockquote>
    <div class="author-photo" role="img" aria-label="Black and white portrait photograph of the author"></div>
    <p class="author-bio">Tom Hollis is a leading futurologist, technologist, inventor, and entrepreneur. With over twenty years of experience in technology and innovation, Tom has travelled the world seeking out and developing new technologies. As a leading voice on the challenges and benefits of tomorrow’s technology, he has advised some of the world’s leading institutions, including the Grand Chancery, regarding technological preparations for the future. He is the recipient of the centennial founder of the season prize and has appeared on numerous technology and philanthropy television programs, as well as presenting Clever Little Marvels on Robotics.</p>
  </section>
  <section class="spine">
    <p class="spine-title">torvanique</p>
  </section>
  <section class="front-cover">
    <h1 class="front-title">torvanique</h1>
    <p class="strapline">The close of human work and how automatons will supplant it.</p>
    <div class="robot-illustration" role="img" aria-label="Glossy white and dark grey humanoid robot standing with one hand extended"></div>
  </section>
</main>
</body>
</html>
```